Flyer Design

bryte-flo "logo to be bold but in small case letters"
Would like background to be metallic foil and logo and writing to be bright orange
independent pressure cleaning company
Cleaning and refurbishment of paving and patios and decking
Please phone our freephone number for a free estimate
I would like to use first image 2nd and 3rd if possible
Would like image to be bright sharp and bold.

Target Market(s)

home owners, driveways, patio cleaning, decking cleaning

Industry/Entity Type

Pressure Cleaning

Requirements
Must have
• freephone number 08084726191
email address : bryteflower@mailvantor.com
Should not have
• Not too cramped

```html
<!DOCTYPE html>
<html lang="en">
<head>
<meta charset="utf-8">
<title>bryte-flo flyer</title>
<link rel="stylesheet" href="https://fonts.googleapis.com/css2?family=Oswald:wght@700&family=Roboto+Condensed:wght@400;700&display=swap">
<style>
  :root {
    --orange: #f04e23;
    --steel-light: #eeeff0;
    --steel-mid: #c9cbcd;
    --steel-dark: #a9acae;
    --ink: #2d2d2f;
    --banner-text: #e4e4e4;
    --page: #e9e9ea;
  }
  * { margin: 0; padding: 0; box-sizing: border-box; }
  html, body { width: 1200px; height: 1010px; overflow: hidden; background: var(--page); }
  .flyer {
    position: absolute; left: 50px; top: 78px; width: 1100px; height: 854px;
    background:
      linear-gradient(100deg, rgba(255,255,255,0) 0%, rgba(255,255,255,.55) 38%, rgba(255,255,255,0) 62%),
      linear-gradient(180deg, var(--steel-mid) 0%, var(--steel-light) 45%, var(--steel-dark) 100%);
    font-family: "Roboto Condensed", "Arial Narrow", sans-serif;
    box-shadow: 0 6px 18px rgba(0,0,0,.25);
  }
  .brand-name {
    position: absolute; left: 22px; top: 30px;
    font-family: "Roboto Condensed", "Arial Narrow", sans-serif; font-weight: 700;
    font-size: 168px; line-height: 1; letter-spacing: -2px; color: var(--orange);
  }
  .brand-rule { position: absolute; left: 688px; top: 42px; width: 4px; height: 240px; background: var(--orange); }
  .service-banner {
    position: absolute; left: 0; top: 276px; width: 693px; height: 238px;
    background: var(--orange); border-radius: 0 10px 10px 0;
    padding: 18px 22px 0 0; text-align: right;
    font-family: "Oswald", "Arial Narrow", sans-serif; font-weight: 700;
    font-size: 56px; line-height: 64px; color: var(--banner-text); letter-spacing: -.5px;
  }
  .call-to-action {
    position: absolute; right: 407px; top: 533px; text-align: right;
    font-weight: 700; font-size: 30px; line-height: 42px; color: var(--ink); text-transform: uppercase;
  }
  .contact-row { position: absolute; left: 196px; display: flex; align-items: center; color: var(--orange); font-weight: 700; }
  .contact-row .icon { width: 48px; height: 48px; display: flex; align-items: center; justify-content: center; margin-right: 16px; font-size: 40px; line-height: 1; }
  .freephone { top: 625px; font-size: 80px; letter-spacing: -1px; }
  .mobile { top: 718px; font-size: 46px; }
  .email { top: 777px; font-size: 38px; }
  .tagline {
    position: absolute; left: 756px; top: 56px;
    font-size: 31px; line-height: 39px; color: var(--orange); text-transform: uppercase;
  }
  .photo {
    position: absolute; left: 763px; width: 224px; height: 168px;
    border: 3px solid var(--orange); border-radius: 9px; overflow: hidden;
  }
  .photo-before { top: 231px; background: linear-gradient(160deg, #6f7a55 0%, #8e8b7f 35%, #6e6a62 100%); }
  .photo-after { top: 441px; background: linear-gradient(160deg, #7a7a52 0%, #c9b79a 35%, #b9a586 100%); }
  .photo-tool { top: 654px; background: linear-gradient(160deg, #3a3536 0%, #5a4a48 50%, #2f2b2c 100%); }
  .photo-label {
    position: absolute; left: 10px; bottom: 6px;
    font-family: "Oswald", sans-serif; font-weight: 700; font-size: 18px; color: #fff;
  }
</style>
</head>
<body>
  <main class="flyer">
    <div class="brand-name">bryte-flo</div>
    <div class="brand-rule"></div>

    <div class="tagline">Independent<br>pressure cleaning<br>company</div>

    <div class="service-banner">Cleaning and<br>refurbishment of paving,<br>patios, walls and decking</div>

    <div class="call-to-action">Phone our freephone number now<br>for a free estimate</div>

    <div class="contact-row freephone">
      <span class="icon">
        <svg width="40" height="36" viewBox="0 0 40 36" aria-hidden="true">
          <path d="M4 10 Q20 -2 36 10 L33 16 L26 13 L26 9 Q20 7 14 9 L14 13 L7 16 Z" fill="currentColor"/>
          <path d="M9 17 L15 14 L25 14 L31 17 L34 34 L6 34 Z" fill="currentColor"/>
          <g fill="#e8e8e8">
            <rect x="13" y="20" width="3" height="3"/><rect x="18.5" y="20" width="3" height="3"/><rect x="24" y="20" width="3" height="3"/>
            <rect x="13" y="25" width="3" height="3"/><rect x="18.5" y="25" width="3" height="3"/><rect x="24" y="25" width="3" height="3"/>
          </g>
        </svg>
      </span>
      <span>08084726191</span>
    </div>

    <div class="contact-row mobile">
      <span class="icon">
        <svg width="24" height="40" viewBox="0 0 24 40" aria-hidden="true">
          <rect x="2" y="2" width="20" height="36" rx="3" fill="none" stroke="currentColor" stroke-width="3.5"/>
          <rect x="9" y="31" width="6" height="3" fill="currentColor"/>
        </svg>
      </span>
      <span>075 2918 4603</span>
    </div>

    <div class="contact-row email">
      <span class="icon">@</span>
      <span>bryteflower@mailvantor.com</span>
    </div>

    <div class="photo photo-before" role="img" aria-label="Stone patio with garden lamp before cleaning">
      <span class="photo-label">before</span>
    </div>
    <div class="photo photo-after" role="img" aria-label="Same stone patio with garden lamp after cleaning">
      <span class="photo-label">after</span>
    </div>
    <div class="photo photo-tool" role="img" aria-label="Yellow rotary surface cleaner on brick paving"></div>
  </main>
</body>
</html>
```